Events Online Video Streaming Company

A website needs to be designed to replace the current website of a company that specialises in providing an online portal for streaming events to users. the current portal exists at: http://www.tazorin.com <- designers can get a "feel" for what they do and the content they require from this existing website.
the current tazorin logo and green color are to be maintined. i will upload an EPS of the logo soon.
The new design needs to highlight the main aspects of what they do: live streaming of events, multiple cameras, online chat, user activity data (like brindle metrics), customised front-ends.
we want the design to be in-between a corporate feel and modern, contemporary. ie. we dont want it to be too corporate (like the current website).
the design must also incorporate the word: fernoskaps as part of their slogan or sub-title.
hi everyone,

```html
<!DOCTYPE html>
<html lang="en">
<head>
<meta charset="utf-8">
<title>Tazorin — Live Event Streaming</title>
<link rel="stylesheet" href="https://fonts.googleapis.com/css2?family=Open+Sans:wght@400;600;700&family=Arimo:wght@400;700&display=swap">
<style>
  :root{
    --green:#86c33b;
    --green-dark:#5f9a22;
    --ink:#231a12;
    --text:#333;
    --muted:#555;
    --line:#d6d6d6;
    --footer-top:#707070;
    --footer-bottom:#4a4a4a;
  }
  *{box-sizing:border-box;margin:0;padding:0}
  html,body{width:1200px;height:1183px;overflow:hidden;background:#fff}
  body{font-family:"Arimo",Arial,sans-serif;color:var(--text)}
  .page{position:relative;width:1200px;height:1183px;overflow:hidden}
  .abs{position:absolute}

  /* header */
  .site-header{left:0;top:0;width:1200px;height:116px;background:linear-gradient(#fff,#eaeaea);border-bottom:1px solid #cfcfcf}
  .brand{left:148px;top:2px;font-family:"Open Sans",sans-serif;font-weight:400;font-size:80px;letter-spacing:-2px;color:var(--green);line-height:1}
  .header-phone{left:919px;top:14px;display:flex;align-items:center;gap:8px;font-family:"Arimo",sans-serif;font-weight:700;font-size:17px;color:#333;white-space:nowrap}
  .main-nav{left:522px;top:70px;width:537px;height:34px;background:linear-gradient(#fff,#e9e9e9);border:1px solid #d0d0d0;border-radius:6px;box-shadow:0 2px 3px rgba(0,0,0,.12);display:flex;align-items:center;padding-left:7px;white-space:nowrap}
  .main-nav a{font-weight:700;font-size:13px;color:#111;text-decoration:none;padding:0 13px;border-left:1px solid #ccc;line-height:16px;white-space:nowrap;flex:none}
  .main-nav a:nth-child(2){border-left:none}
  .main-nav a.active{background:linear-gradient(#8cc84a,#5c9a22);color:#fff;border:none;border-radius:3px;padding:4px 11px;margin-right:10px}

  /* hero */
  .hero-band{left:0;top:117px;width:1200px;height:455px;background:var(--green);box-shadow:inset 0 -6px 8px rgba(0,0,0,.12)}
  .hero-image{left:140px;top:137px;width:918px;height:422px;background:linear-gradient(135deg,#e6dccd 0%,#d7c9b2 40%,#c9b99e 60%,#9fbd5c 85%,#8cb84a 100%)}
  .hero-caption{left:140px;top:394px;width:293px;height:165px;background:rgba(70,60,50,.6);padding:6px 8px 0 14px;overflow:hidden}
  .hero-caption h1{font-family:"Open Sans",sans-serif;font-weight:700;font-size:38px;color:var(--green);letter-spacing:.5px;line-height:42px}
  .hero-caption p{font-size:14px;line-height:24px;color:#fff;margin-top:4px;letter-spacing:-.1px}

  /* features */
  .feature-band{left:0;top:573px;width:1200px;height:191px;background:linear-gradient(#d9d9d9,#fff 80%)}
  .feature-card{top:589px;width:216px;height:123px;background:linear-gradient(#fff 40%,#cfcfcf);border:1px solid #d2d2d2;border-radius:8px;box-shadow:0 6px 6px -3px rgba(0,0,0,.15);padding:8px 8px 0 9px}
  .feature-card h2{font-family:"Open Sans",sans-serif;font-weight:600;font-size:20px;color:var(--ink);letter-spacing:-.3px;line-height:26px;white-space:nowrap}
  .feature-card h2 span{color:var(--green)}
  .feature-card p{font-size:12px;line-height:17px;color:#222;margin-top:5px}
  .read-more{position:absolute;right:10px;bottom:9px;display:flex;align-items:center;gap:6px;font-size:12px;font-weight:700;color:#555;text-decoration:underline}
  .plus{width:15px;height:15px;border-radius:50%;background:#777;color:#fff;font-size:13px;line-height:15px;text-align:center;text-decoration:none;font-weight:700}

  /* info */
  .info-band{left:0;top:764px;width:1200px;height:298px;background:#f4f4f4}
  .col h3{font-family:"Open Sans",sans-serif;font-weight:700;font-size:20px;color:var(--ink);letter-spacing:-.3px;height:40px;border-bottom:1px solid var(--line);line-height:40px;white-space:nowrap}
  .col h3 span{color:var(--green)}
  .col h3 .inline-brand{font-weight:400;font-size:30px;letter-spacing:-1px}
  .welcome{left:140px;top:784px;width:285px}
  .welcome p{font-size:11.4px;line-height:18px;color:#333;margin-top:9px;text-align:justify;letter-spacing:.2px}
  .link-more{display:block;text-align:right;font-size:12px;font-weight:700;color:#555;text-decoration:underline;margin-top:6px;padding-right:4px}
  .divider{top:790px;width:1px;height:250px;background:linear-gradient(rgba(0,0,0,0),#ddd,rgba(0,0,0,0))}
  .testimonials{left:456px;top:784px;width:285px}
  .quote{border-bottom:1px dashed #ccc;padding:10px 2px 4px}
  .quote p{font-size:11.4px;line-height:18px;color:#666}
  .quote cite{display:block;text-align:right;font-style:normal;font-weight:700;font-size:11.4px;color:#111;padding-right:6px}
  .quote:last-of-type{border-bottom:none}
  .contact{left:773px;top:784px;width:285px}
  .field{display:flex;align-items:flex-start;margin-top:10px}
  .field:first-of-type{margin-top:14px}
  .field label{width:68px;font-size:12.5px;color:#444;padding:7px 0 0 5px}
  .field .input{width:217px;height:24px;background:#fff;border:1px solid #c9c9c9;border-radius:3px;box-shadow:inset 0 1px 2px rgba(0,0,0,.08)}
  .field .input.tall{height:56px}
  .submit{position:absolute;right:0;top:228px;width:68px;height:26px;background:linear-gradient(#555,#1f1f1f);color:#fff;border-radius:3px;font-weight:700;font-size:13px;text-align:center;line-height:26px}

  /* footer */
  .site-footer{left:0;top:1062px;width:1200px;height:121px;background:linear-gradient(var(--footer-top),var(--footer-bottom));border-top:2px solid #9a9a9a}
  .footer-nav{left:141px;top:1080px;display:flex;font-size:12px;font-weight:700;color:#fff;white-space:nowrap}
  .footer-nav a{color:#fff;text-decoration:none;padding:0 12px;border-left:1px solid #ddd;line-height:12px}
  .footer-nav a:first-child{padding-left:0;border-left:none}
  .footer-contact{left:139px;top:1113px;display:flex;gap:18px;align-items:center;font-size:12.5px;font-weight:700;color:#fff;white-space:nowrap}
  .footer-contact span{display:flex;align-items:center;gap:8px}
  .copyright{left:142px;top:1150px;font-size:11.5px;color:#fff}
  .footer-brand{left:900px;top:1068px;font-family:"Open Sans",sans-serif;font-weight:400;font-size:40px;letter-spacing:-1px;color:#fff}
  .social{left:901px;top:1134px;display:flex;gap:3px}
  .social i{display:block;width:27px;height:27px;border-radius:3px;background:#9a9a9a}
</style>
</head>
<body>
<div class="page">

  <header class="site-header abs"></header>
  <div class="brand abs">tazorin</div>
  <div class="header-phone abs">
    <svg width="16" height="22" viewBox="0 0 16 22"><path d="M4 1 L7 6 L5 8 C6 12 8 15 10 16 L12 14 L15 18 L12 21 C6 20 1 12 1 4 Z" fill="#86c33b"/></svg>
    1300 555 019
  </div>
  <nav class="main-nav abs">
    <a class="active">Home</a><a>Features</a><a>Applications</a><a>The Team</a><a>Support</a><a>Contact Us</a>
  </nav>

  <div class="hero-band abs"></div>
  <div class="hero-image abs" role="img" aria-label="Photo of a woman lying on a green rug in a living room, smiling while using a laptop"></div>
  <div class="hero-caption abs">
    <h1>FERNOSKAPS</h1>
    <p>Lorem ipsum dolor sit amet, consectetuer adipiscing elit, sed diam nonummy nibh euismod tincidunt ut laoreet dolore magna aliquam erat volutpat.</p>
  </div>

  <div class="feature-band abs"></div>
  <section class="feature-card abs" style="left:141px">
    <h2><span>Live</span> Streaming</h2>
    <p>Ut wisi enim ad minim veniamquis nostrud exerci tation ullamcorperi t lobortis nisl ut aliquip ex ea com.</p>
    <a class="read-more">Read more <b class="plus">+</b></a>
  </section>
  <section class="feature-card abs" style="left:375px">
    <h2><span>Multiple</span> Cameras</h2>
    <p>Ut wisi enim ad minim veniamquis nostrud exerci tation ullamcorperi t lobortis nisl ut aliquip ex ea com.</p>
    <a class="read-more">Read more <b class="plus">+</b></a>
  </section>
  <section class="feature-card abs" style="left:609px">
    <h2><span>Online</span> Chat</h2>
    <p>Ut wisi enim ad minim veniamquis nostrud exerci tation ullamcorperi t lobortis nisl ut aliquip ex ea com.</p>
    <a class="read-more">Read more <b class="plus">+</b></a>
  </section>
  <section class="feature-card abs" style="left:844px">
    <h2><span>User Activity</span> Data</h2>
    <p>Ut wisi enim ad minim veniamquis nostrud exerci tation ullamcorperi t lobortis nisl ut aliquip ex ea com.</p>
    <a class="read-more">Read more <b class="plus">+</b></a>
  </section>

  <div class="info-band abs"></div>
  <section class="col welcome abs">
    <h3>Welcome To <span class="inline-brand">tazorin</span></h3>
    <p>Lorem ipsum dolor sit amet, consectetuer adipiscing elit, sed diam nonummy nibh euismod tincidunt ut laoreet dolore magna aliquam erat volutpat. Ut wisi enim ad minim veniam, quis nostrud exerci tation ullamcorper suscipit lobortis nisl ut aliquip ex ea commodo consequat. Duis autem vel eum iriure dolor in hendrerit in amet sit vulputate velit esse molestie consequat, vel illum dolore eu feugiat nulla facilisis at vero it addipsing amet construction. Duis aute irure dolor in reprehenderit in voluptate.</p>
    <a class="link-more">Read more »</a>
  </section>
  <div class="divider abs" style="left:441px"></div>
  <section class="col testimonials abs">
    <h3>Client <span>Testimonials</span></h3>
    <div class="quote"><p>"Duis aute irure dolor in reprehenderit in voluptate velit esse cillum dolore eu fugiat nulla pariatur amet cons"</p><cite>- Lorem Ipsum</cite></div>
    <div class="quote"><p>"Duis aute irure dolor in reprehenderit in voluptate velit esse cillum dolore eu fugiat nulla pariatur amet cons"</p><cite>- Lorem Ipsum</cite></div>
    <div class="quote"><p>"Duis aute irure dolor in reprehenderit in voluptate velit esse cillum dolore eu fugiat nulla pariatur amet cons"</p></div>
    <a class="link-more" style="margin-top:12px">Read more »</a>
  </section>
  <div class="divider abs" style="left:757px"></div>
  <section class="col contact abs">
    <h3>Quick <span>Contact</span></h3>
    <div class="field"><label>Name</label><div class="input"></div></div>
    <div class="field"><label>Email</label><div class="input"></div></div>
    <div class="field"><label>Phone</label><div class="input"></div></div>
    <div class="field"><label>Message</label><div class="input tall"></div></div>
    <div class="submit">Submit</div>
  </section>

  <footer class="site-footer abs"></footer>
  <nav class="footer-nav abs"><a>Home</a><a>Features</a><a>Applications</a><a>The Team</a><a>Support</a><a>Contact Us</a></nav>
  <div class="footer-contact abs">
    <span><svg width="14" height="18" viewBox="0 0 14 18"><path d="M7 0 C3 0 0 3 0 7 C0 11 7 18 7 18 C7 18 14 11 14 7 C14 3 11 0 7 0 Z" fill="#fff"/><circle cx="7" cy="7" r="2.5" fill="#666"/></svg>Dignissim Sit Amet Sit Amet Lorem.</span>
    <span><svg width="16" height="11" viewBox="0 0 16 11"><rect width="16" height="11" rx="1" fill="#fff"/><path d="M0 0 L8 6 L16 0" stroke="#666" fill="none"/></svg>info@tazorin.com</span>
    <span><svg width="13" height="16" viewBox="0 0 16 22"><path d="M4 1 L7 6 L5 8 C6 12 8 15 10 16 L12 14 L15 18 L12 21 C6 20 1 12 1 4 Z" fill="#fff"/></svg>1300 555 019</span>
  </div>
  <div class="copyright abs">Copyright © 2013 Tazorin. All rights reserved.</div>
  <div class="footer-brand abs">tazorin</div>
  <div class="social abs"><i></i><i></i><i></i><i></i><i></i></div>

</div>
</body>
</html>
```